a classfull design for our clothing brand packaging

Hi,

I like to have our logo in gold with also our website www.lecomtedubrel.be on it. background i would like matt black.
also the instagram and facebook logo should be on the package
The overall package should reflect class and quality
Overall black and grey tints except our logo.
The picture of our city antwerp should be worked into the design
The goal is to get a design to put on our sendboxes we will send to our customers.

box info

220mm x 157mm x 105mm

thank you in advance!

regards
le Comte du brel

Target Market(s)

young adults - adults men

Industry/Entity Type

Clothing

Font styles to use
Script

Colors
ffc214

Requirements
Must have
• a classic and luxury look

```html
<!DOCTYPE html>
<html lang="en">
<head>
<meta charset="utf-8">
<title>le Comte du brel – packaging</title>
<link rel="stylesheet" href="https://fonts.googleapis.com/css2?family=Parisienne&display=swap">
<style>
  :root {
    --matt-black: #0a0a0a;
    --deep-black: #000000;
    --gold-dark: #c1893a;
    --gold-light: #e9c65a;
    --ink: #050505;
  }
  html, body {
    margin: 0;
    padding: 0;
    width: 812px;
    height: 1200px;
    overflow: hidden;
    background: var(--matt-black);
  }
  .package-face {
    position: relative;
    width: 812px;
    height: 1200px;
    background: var(--matt-black);
    overflow: hidden;
  }
  .brand-watermark {
    position: absolute;
    left: -170px;
    top: 150px;
    margin: 0;
    font-family: "Parisienne", cursive;
    font-weight: 400;
    font-size: 620px;
    line-height: 1;
    white-space: nowrap;
    color: var(--deep-black);
    user-select: none;
  }
  .gold-band {
    position: absolute;
    left: 0;
    top: 967px;
    width: 561px;
    height: 96px;
    background: linear-gradient(125deg,
      var(--gold-dark) 0%,
      var(--gold-dark) 22%,
      var(--gold-light) 29%,
      var(--gold-light) 32%,
      var(--gold-dark) 38%,
      var(--gold-dark) 40%,
      var(--gold-light) 47%,
      var(--gold-light) 100%);
  }
  .band-brand-name {
    position: absolute;
    left: 362px;
    top: 50%;
    transform: translateY(-50%);
    margin: 0;
    font-family: "Parisienne", cursive;
    font-weight: 400;
    font-size: 26px;
    line-height: 1;
    white-space: nowrap;
    color: var(--ink);
  }
</style>
</head>
<body>
  <main class="package-face">
    <p class="brand-watermark" aria-hidden="true">le Comte du brel</p>
    <section class="gold-band">
      <p class="band-brand-name">le Comte du brel</p>
    </section>
  </main>
</body>
</html>
```